New Organic Skin Care Line Needs to Design a Product Label

***THE WINNER OF THIS PROJECT WILL MOST LIKELY BECOME THE EXCLUSIVE DESIGNER FOR OUR OTHER PRODUCT LABELS***

We need a label design for a new organic skin care product line called "Maple Dune Festoon." This specific product is a 100% pure organic coconut oil. It's used for skin hydration, protection, and makeup removal.

Info to include on front label:

1. Logo: Maple Dune Festoon (attached)
2. Product Name: Pure Coconut Oil (emphasize "organic" somewhere)
3. Slogan: Hydrate your skin and hair.
4. Size: 8 FL OZ 236mL

Attached is:

1. The brand logo "Maple Dune Festoon" with a white background.
2. An image of the bottle we will use.
3. An image of the bottle with lines to show the size and placement of the label.
4. The brand logo "Maple Dune Festoon" with a black background. (photoshop file)

What we need:

A simple mock up of the front side of the label on the bottle. We first want to know what it will look like on the bottle given the size and dimensions.

- We would like one label with a white background (including the logo with a white background).
- We would like a second label with a black background (including the logo with a black background, just need to make the black font white instead of black).

We can get a great idea of what to expect from the front side of the label so we will complete the back side once we identify a winner.
Updates

Apologies, but we are now using a different bottle. The previous one is now discontinued. Please view the two most recent images uploaded. One is an image of the new bottle by itself. The other is an image of that bottle with instructions. Please use your most recent designs on the new bottle. Feel free to make any modifications you see fit to compliment the new bottle shape. Added Friday, March 18, 2016

Project Deadline Extended
Reason: We are still working with the label company to finalize the size. Once the size is confirmed we will have to tweak labels based on finalized measurements.

Target Market(s)

Women, 18-70

Industry/Entity Type

Skin Care Product

Font styles to use
Decorative
Script

Requirements
Must have
• -"shabby sheek" and "cute" theme
• -soft organic feel
• -the ingredients are organic, pure, and natural. That should be an essence of the label.

```html
<!DOCTYPE html>
<html lang="en">
<head>
<meta charset="utf-8">
<title>Maple Dune Festoon – Pure Organic Coconut Oil Labels</title>
<link href="https://fonts.googleapis.com/css2?family=Antonio:wght@100&family=Montserrat:wght@300;400&family=Italianno&family=Cinzel:wght@400&display=swap" rel="stylesheet">
<style>
  :root {
    --tan: #e3b577;
    --tan-edge: #b98f5a;
    --tan-text: #c9a273;
    --pink: #d6336c;
    --ink: #111111;
    --paper: #ffffff;
    --night: #000000;
    --glass: #e6e7e8;
    --tube: #b8b9bb;
    --frame: #b3b3b3;
  }
  html, body {
    margin: 0;
    padding: 0;
    width: 1200px;
    height: 1200px;
    overflow: hidden;
    background: var(--paper);
  }
  .sheet {
    position: relative;
    width: 1200px;
    height: 1200px;
  }
  .flat-label {
    position: absolute;
    top: 123px;
    width: 522px;
    height: 247px;
    overflow: hidden;
    box-sizing: border-box;
    border: 1px solid var(--frame);
    text-align: center;
  }
  .flat-label--white { left: 69px; background: var(--paper); }
  .flat-label--black { left: 610px; background: var(--night); }

  .seal {
    position: absolute;
    left: 175px;
    top: -21px;
    width: 172px;
    height: 172px;
    border-radius: 50%;
    background: var(--tan);
    border: 1px dashed var(--tan-edge);
    box-sizing: border-box;
  }
  .flat-label--black .seal { border-color: #f3dcb8; }

  .line {
    position: absolute;
    left: 0;
    right: 0;
    margin: 0;
    line-height: 1;
  }
  .kicker {
    top: 15px;
    font: 300 14px "Montserrat", sans-serif;
    color: var(--paper);
  }
  .product {
    top: 29px;
    font: 100 40px "Antonio", sans-serif;
    color: var(--paper);
    letter-spacing: 1px;
  }
  .product-big {
    top: 65px;
    font: 100 56px "Antonio", sans-serif;
    color: var(--paper);
    letter-spacing: 2px;
  }
  .slogan {
    top: 137px;
    font: 34px "Italianno", cursive;
    color: var(--tan-text);
  }
  .flat-label--black .slogan { color: var(--paper); }
  .brand {
    top: 204px;
    font: 400 14px "Cinzel", serif;
    letter-spacing: 3px;
    color: var(--pink);
  }

  .mockups {
    position: absolute;
    left: 0;
    top: 0;
  }
  .t-kicker { font: 300 11px "Montserrat", sans-serif; fill: var(--paper); }
  .t-kicker-lg { font: 300 12px "Montserrat", sans-serif; fill: var(--paper); }
  .t-product { font: 100 31px "Antonio", sans-serif; fill: var(--paper); }
  .t-product-lg { font: 100 37px "Antonio", sans-serif; fill: var(--paper); }
  .t-big { font: 100 44px "Antonio", sans-serif; fill: var(--paper); }
  .t-big-lg { font: 100 50px "Antonio", sans-serif; fill: var(--paper); }
  .t-slogan { font: 22px "Italianno", cursive; fill: var(--tan-text); }
  .t-slogan-light { font: 22px "Italianno", cursive; fill: var(--paper); }
  .t-slogan-small { font: 15px "Italianno", cursive; fill: var(--paper); }
  .t-brand { font: 400 7.5px "Cinzel", serif; letter-spacing: 1.5px; fill: var(--pink); }
  .t-size { font: 400 8.5px "Montserrat", sans-serif; fill: var(--ink); }
</style>
</head>
<body>
<main class="sheet">

  <section class="flat-label flat-label--white" aria-label="Flat label, white version">
    <div class="seal"></div>
    <p class="line kicker">PURE ORGANIC</p>
    <p class="line product">COCONUT</p>
    <p class="line product-big">OIL</p>
    <p class="line slogan">Hydrate your skin and hair.</p>
    <p class="line brand">MAPLE DUNE FESTOON</p>
  </section>

  <section class="flat-label flat-label--black" aria-label="Flat label, black version">
    <div class="seal"></div>
    <p class="line kicker">PURE ORGANIC</p>
    <p class="line product">COCONUT</p>
    <p class="line product-big">OIL</p>
    <p class="line slogan">Hydrate your skin and hair.</p>
    <p class="line brand">MAPLE DUNE FESTOON</p>
  </section>

  <svg class="mockups" width="1200" height="1200" viewBox="0 0 1200 1200" aria-label="Labels shown on the bottle">
    <defs>
      <path id="bottle-shape" d="M84,8 Q84,0 96,0 L144,0 Q156,0 156,8 L156,40 L150,48 L152,120 Q154,230 170,290 Q186,340 214,390 Q234,430 234,450 Q234,500 190,530 Q150,548 120,548 Q90,548 50,530 Q6,500 6,450 Q6,430 26,390 Q54,340 70,290 Q86,230 88,120 L90,48 L84,40 Z"/>
      <clipPath id="bottle-clip"><use href="#bottle-shape"/></clipPath>
      <clipPath id="label-clip"><rect x="0" y="322" width="240" height="240"/></clipPath>
      <radialGradient id="label-white" cx="0.5" cy="0.4" r="0.6">
        <stop offset="0.5" stop-color="#ffffff"/>
        <stop offset="1" stop-color="#cfd0d2"/>
      </radialGradient>
      <radialGradient id="label-black" cx="0.5" cy="0.45" r="0.6">
        <stop offset="0" stop-color="#4a4a4a"/>
        <stop offset="0.8" stop-color="#0b0b0b"/>
      </radialGradient>
    </defs>

    <!-- White label, seal on top -->
    <g class="bottle" transform="translate(24,560)">
      <use href="#bottle-shape" fill="var(--glass)"/>
      <rect x="118" y="290" width="4" height="32" fill="var(--tube)"/>
      <g clip-path="url(#bottle-clip)">
        <rect x="0" y="322" width="240" height="240" fill="url(#label-white)"/>
        <g clip-path="url(#label-clip)">
          <circle cx="120" cy="372" r="67" fill="var(--tan)" stroke="var(--tan-edge)" stroke-dasharray="2 2"/>
        </g>
      </g>
      <text class="t-kicker" x="120" y="341" text-anchor="middle">PURE ORGANIC</text>
      <text class="t-product" x="120" y="374" text-anchor="middle">COCONUT</text>
      <text class="t-big" x="120" y="422" text-anchor="middle">OIL</text>
      <text class="t-slogan" x="120" y="456" text-anchor="middle">Hydrate your skin and hair.</text>
      <text class="t-brand" x="120" y="500" text-anchor="middle">MAPLE DUNE FESTOON</text>
      <text class="t-size" x="120" y="529" text-anchor="middle">8 FL OZ 236mL</text>
    </g>

    <!-- White label, seal at base -->
    <g class="bottle" transform="translate(294,560)">
      <use href="#bottle-shape" fill="var(--glass)"/>
      <rect x="118" y="290" width="4" height="32" fill="var(--tube)"/>
      <g clip-path="url(#bottle-clip)">
        <rect x="0" y="322" width="240" height="240" fill="url(#label-white)"/>
        <circle cx="120" cy="488" r="86" fill="var(--tan)" stroke="var(--tan-edge)" stroke-dasharray="2 2"/>
      </g>
      <text class="t-brand" x="120" y="364" text-anchor="middle">MAPLE DUNE FESTOON</text>
      <text class="t-kicker-lg" x="120" y="438" text-anchor="middle">PURE ORGANIC</text>
      <text class="t-product-lg" x="120" y="471" text-anchor="middle">COCONUT</text>
      <text class="t-big-lg" x="120" y="516" text-anchor="middle">OIL</text>
      <text class="t-slogan-small" x="120" y="530" text-anchor="middle">Hydrate your skin and hair.</text>
    </g>

    <!-- Black label, seal on top -->
    <g class="bottle" transform="translate(618,560)">
      <use href="#bottle-shape" fill="var(--glass)"/>
      <rect x="118" y="290" width="4" height="32" fill="var(--tube)"/>
      <g clip-path="url(#bottle-clip)">
        <rect x="0" y="322" width="240" height="240" fill="url(#label-black)"/>
        <g clip-path="url(#label-clip)">
          <circle cx="120" cy="372" r="67" fill="var(--tan)"/>
        </g>
      </g>
      <text class="t-kicker" x="120" y="341" text-anchor="middle">PURE ORGANIC</text>
      <text class="t-product" x="120" y="374" text-anchor="middle">COCONUT</text>
      <text class="t-big" x="120" y="422" text-anchor="middle">OIL</text>
      <text class="t-slogan-light" x="120" y="451" text-anchor="middle">Hydrate your skin and hair.</text>
      <text class="t-brand" x="120" y="500" text-anchor="middle">MAPLE DUNE FESTOON</text>
    </g>

    <!-- Black label, seal at base -->
    <g class="bottle" transform="translate(888,560)">
      <use href="#bottle-shape" fill="var(--glass)"/>
      <rect x="118" y="290" width="4" height="32" fill="var(--tube)"/>
      <g clip-path="url(#bottle-clip)">
        <rect x="0" y="322" width="240" height="240" fill="url(#label-black)"/>
        <circle cx="120" cy="488" r="86" fill="var(--tan)"/>
      </g>
      <text class="t-brand" x="120" y="364" text-anchor="middle">MAPLE DUNE FESTOON</text>
      <text class="t-kicker-lg" x="120" y="438" text-anchor="middle">PURE ORGANIC</text>
      <text class="t-product-lg" x="120" y="471" text-anchor="middle">COCONUT</text>
      <text class="t-big-lg" x="120" y="516" text-anchor="middle">OIL</text>
      <text class="t-slogan-small" x="120" y="530" text-anchor="middle">Hydrate your skin and hair.</text>
    </g>
  </svg>

</main>
</body>
</html>
```